Minimalist Planner/Journal Design

We need a planner/journal designed for daily use in a small group. I've attached a requirements document that outlines what every page needs to have on it. I've also attached a basic rough draft that we had made in Canva but the draft needs to be redesigned to look more in line with the style we need. I've attached some sample pages from some planners we like the style of. Feel free to add your own creativity and stylistic choices but keep in mind we are trying to get a very 'clean and minimalist design'. The deliverables should be both a pdf of the 8 planner pages, as well as the photoshop/gimp/illustrator files for the project.

Font styles to use
Other font styles liked:
• You choose, but we prefer thin , basic/minimal font faces

Requirements
Must have
• Minimal Design

```html
<!DOCTYPE html>
<html lang="en">
<head>
<meta charset="utf-8">
<title>Monthly Planner Page</title>
<link rel="stylesheet" href="https://fonts.googleapis.com/css2?family=Source+Sans+3:wght@300;400&display=swap">
<style>
  :root {
    --backdrop: #808080;
    --paper: #ffffff;
    --ink: #333333;
    --rule: #8a8a8a;
    --grid: #c8c8c8;
    --dots: #ababab;
    --label: #8a8a8a;
  }
  html, body {
    margin: 0;
    padding: 0;
    width: 1079px;
    height: 1200px;
    overflow: hidden;
    background: var(--backdrop);
  }
  .planner-page {
    display: block;
    width: 1079px;
    height: 1200px;
  }
  .sheet { fill: var(--paper); }
  .month-label {
    font-family: "Source Sans 3", sans-serif;
    font-weight: 400;
    font-size: 27px;
    fill: var(--ink);
  }
  .month-line { stroke: var(--grid); stroke-width: 2; }
  .header-rule { stroke: var(--rule); stroke-width: 3; }
  .calendar-grid line,
  .calendar-grid rect,
  .day-tab {
    fill: none;
    stroke: var(--grid);
    stroke-width: 3;
  }
  .notes-label {
    font-family: "Source Sans 3", sans-serif;
    font-weight: 300;
    font-size: 23px;
    fill: var(--label);
  }
  .note-line {
    stroke: var(--dots);
    stroke-width: 2.5;
    stroke-dasharray: 2.5 3.5;
  }
</style>
</head>
<body>
<svg class="planner-page" viewBox="0 0 1820 2024" xmlns="http://www.w3.org/2000/svg">
  <defs>
    <path id="day-tab" class="day-tab" d="M2 0 V19 A14 14 0 0 0 30 19 V0"/>
  </defs>

  <path class="sheet" d="M255 164 H1505 A60 60 0 0 1 1565 224 V1800 A60 60 0 0 1 1505 1860 H255 Z"/>

  <g class="page-header">
    <text class="month-label" x="315" y="251">MONTH:</text>
    <line class="month-line" x1="433" y1="254" x2="658" y2="254"/>
    <line class="header-rule" x1="315" y1="288" x2="1505" y2="288"/>
  </g>

  <g class="calendar-grid">
    <rect x="315" y="370" width="1190" height="875"/>
    <line x1="485" y1="370" x2="485" y2="1245"/>
    <line x1="655" y1="370" x2="655" y2="1245"/>
    <line x1="825" y1="370" x2="825" y2="1245"/>
    <line x1="995" y1="370" x2="995" y2="1245"/>
    <line x1="1165" y1="370" x2="1165" y2="1245"/>
    <line x1="1335" y1="370" x2="1335" y2="1245"/>
    <line x1="315" y1="516" x2="1505" y2="516"/>
    <line x1="315" y1="662" x2="1505" y2="662"/>
    <line x1="315" y1="807" x2="1505" y2="807"/>
    <line x1="315" y1="953" x2="1505" y2="953"/>
    <line x1="315" y1="1099" x2="1505" y2="1099"/>
  </g>

  <g class="day-tabs">
    <use href="#day-tab" x="315" y="371"/><use href="#day-tab" x="485" y="371"/><use href="#day-tab" x="655" y="371"/><use href="#day-tab" x="825" y="371"/><use href="#day-tab" x="995" y="371"/><use href="#day-tab" x="1165" y="371"/><use href="#day-tab" x="1335" y="371"/>
    <use href="#day-tab" x="315" y="517"/><use href="#day-tab" x="485" y="517"/><use href="#day-tab" x="655" y="517"/><use href="#day-tab" x="825" y="517"/><use href="#day-tab" x="995" y="517"/><use href="#day-tab" x="1165" y="517"/><use href="#day-tab" x="1335" y="517"/>
    <use href="#day-tab" x="315" y="663"/><use href="#day-tab" x="485" y="663"/><use href="#day-tab" x="655" y="663"/><use href="#day-tab" x="825" y="663"/><use href="#day-tab" x="995" y="663"/><use href="#day-tab" x="1165" y="663"/><use href="#day-tab" x="1335" y="663"/>
    <use href="#day-tab" x="315" y="808"/><use href="#day-tab" x="485" y="808"/><use href="#day-tab" x="655" y="808"/><use href="#day-tab" x="825" y="808"/><use href="#day-tab" x="995" y="808"/><use href="#day-tab" x="1165" y="808"/><use href="#day-tab" x="1335" y="808"/>
    <use href="#day-tab" x="315" y="954"/><use href="#day-tab" x="485" y="954"/><use href="#day-tab" x="655" y="954"/><use href="#day-tab" x="825" y="954"/><use href="#day-tab" x="995" y="954"/><use href="#day-tab" x="1165" y="954"/><use href="#day-tab" x="1335" y="954"/>
    <use href="#day-tab" x="315" y="1100"/><use href="#day-tab" x="485" y="1100"/><use href="#day-tab" x="655" y="1100"/><use href="#day-tab" x="825" y="1100"/><use href="#day-tab" x="995" y="1100"/><use href="#day-tab" x="1165" y="1100"/><use href="#day-tab" x="1335" y="1100"/>
  </g>

  <g class="notes">
    <text class="notes-label" x="314" y="1334">NOTES.</text>
    <line class="note-line" x1="316" y1="1370" x2="1504" y2="1370"/>
    <line class="note-line" x1="316" y1="1423" x2="1504" y2="1423"/>
    <line class="note-line" x1="316" y1="1477" x2="1504" y2="1477"/>
    <line class="note-line" x1="316" y1="1530" x2="1504" y2="1530"/>
    <line class="note-line" x1="316" y1="1584" x2="1504" y2="1584"/>
    <line class="note-line" x1="316" y1="1637" x2="1504" y2="1637"/>
    <line class="note-line" x1="316" y1="1691" x2="1504" y2="1691"/>
    <line class="note-line" x1="316" y1="1744" x2="1504" y2="1744"/>
  </g>
</svg>
</body>
</html>
```